D&L's Golden Coop Needs a Poster Design

Fast Food Take out fried chicken, fries, drinks etc etc.
I need a poser to draw attention to customers while in line.
It is similar to a "Fenwicks" fast food concept, so the customers never enter the building. All sales are done from the window, so as they are standing outside in line, I would like to interest them with a poster of some sort as an introduction to the store and what is being offered . The poster will sit in a large window.
I have a logo which I will attach.... this may help with ideas also. I am open to any ideas. Logo may or may not be included in poster, but not a necessity.
I found another picture I like.....Will send attachment Added Friday, August 14, 2015
Fast Food : Customers/ Family Friendly

```html
<!DOCTYPE html>
<html lang="en">
<head>
<meta charset="utf-8">
<title>D&amp;L's Golden Coop – Fried Chicken &amp; Fries</title>
<link rel="stylesheet" href="https://fonts.googleapis.com/css2?family=Oswald:wght@600&family=Playfair+Display:wght@400&family=Great+Vibes&display=swap">
<style>
  :root {
    --bg-center: #3a404d;
    --bg-edge: #1c2029;
    --headline-grey: #c9c9c9;
    --fries-white: #f4f1ec;
    --amp-red: #8f1d1c;
    --dot-red: #9b2f2a;
    --dot-tan: #b07a3c;
    --dot-olive: #6f7a2c;
    --dot-orange: #c25a1e;
    --dot-maroon: #6e1a1c;
  }
  * { margin: 0; padding: 0; box-sizing: border-box; }
  html, body { width: 847px; height: 1200px; overflow: hidden; }
  .poster {
    position: relative;
    width: 847px; height: 1200px;
    overflow: hidden;
    background: radial-gradient(ellipse at 50% 45%, var(--bg-center) 0%, var(--bg-edge) 85%);
  }
  .headline {
    position: absolute; left: 0; width: 100%;
    text-align: center;
    font-family: "Oswald", sans-serif;
    font-weight: 600;
    color: var(--headline-grey);
    line-height: 1;
    letter-spacing: 4px;
  }
  .headline--fried { top: 18px; font-size: 190px; }
  .headline--chicken { top: 196px; font-size: 168px; letter-spacing: 2px; }
  .plate-photo {
    position: absolute;
    left: 95px; top: 375px;
    width: 660px; height: 430px;
  }
  .ampersand {
    position: absolute;
    left: 300px; top: 590px;
    font-family: "Great Vibes", cursive;
    font-size: 340px;
    line-height: 1;
    color: var(--amp-red);
  }
  .brand {
    position: absolute;
    left: 590px; top: 700px;
    display: flex; align-items: center; gap: 8px;
  }
  .brand__mark {
    width: 16px; height: 16px;
    background: var(--fries-white);
  }
  .brand__name {
    font-family: "Oswald", sans-serif;
    font-weight: 600;
    font-size: 22px;
    color: var(--fries-white);
    white-space: nowrap;
  }
  .headline--fries {
    position: absolute; left: 0; top: 820px; width: 100%;
    text-align: center;
    font-family: "Playfair Display", serif;
    font-weight: 400;
    font-size: 250px;
    line-height: 1;
    color: var(--fries-white);
    letter-spacing: 12px;
    transform: scaleY(1.32);
    transform-origin: top center;
  }
  .dots { position: absolute; left: 0; top: 1095px; width: 847px; height: 105px; }
</style>
</head>
<body>
<main class="poster">
  <h1 class="headline headline--fried">FRIED</h1>
  <h2 class="headline headline--chicken">CHICKEN</h2>

  <svg class="plate-photo" viewBox="0 0 660 430" role="img" aria-label="Photo of a plate with fried chicken pieces, french fries and a biscuit">
    <defs>
      <radialGradient id="plateTone" cx="50%" cy="50%" r="55%">
        <stop offset="0%" stop-color="#c98a3c"/>
        <stop offset="60%" stop-color="#b0672a"/>
        <stop offset="100%" stop-color="#e8e4dc"/>
      </radialGradient>
    </defs>
    <ellipse cx="330" cy="225" rx="325" ry="200" fill="url(#plateTone)"/>
  </svg>

  <div class="ampersand" aria-hidden="true">&amp;</div>

  <div class="brand">
    <span class="brand__mark"></span>
    <span class="brand__name">D&amp;L's Golden Coop</span>
  </div>

  <h2 class="headline--fries">FRIES</h2>

  <svg class="dots" viewBox="0 0 847 105" aria-hidden="true">
    <circle cx="72" cy="60" r="44" fill="var(--dot-red)"/>
    <circle cx="246" cy="60" r="44" fill="var(--dot-tan)"/>
    <circle cx="420" cy="60" r="44" fill="var(--dot-olive)"/>
    <circle cx="594" cy="60" r="44" fill="var(--dot-orange)"/>
    <circle cx="768" cy="60" r="44" fill="var(--dot-maroon)"/>
  </svg>
</main>
</body>
</html>
```